Social Media Marketing Website

I would like someone to finish off my website as the previous designer has decided otherwise. I like the current layout but it can be better. I also want the site to reflect my portfolio uploaded on each brand I have worked with. I need to upload videos and make the website responsive and load very quickly. It also needs to be mobile and tablet friendly. I know my way around websites and what is current. my website is www.plomantix.com

Target Market(s)

Business seeking brand consultation and ecommerce solutions

Industry/Entity Type

Digital Marketing

Coding

Coded - Design and coding required

Number of Pages Required

5+ page

Other font styles liked:
• Bebas Neue

Colors
ffffff
aaaaaa
f5f5f5
fffbf0

Requirements
Must have
• Fast loading website that is easy to navigate. Can withstand video content and high res pictures. Easy backend to operate. Google Analytics Set Up.
Nice to have
• Interactive site
Should not have
• Complex design that is not easy to navigate for the non tech savvy visitor.

```html
<!DOCTYPE html>
<html lang="en">
<head>
<meta charset="utf-8">
<title>Harlow Crest Studio</title>
<link rel="stylesheet" href="https://fonts.googleapis.com/css2?family=Bebas+Neue&family=Roboto:wght@400;500&display=swap">
<style>
:root{
  --white:#ffffff;
  --mid:#aaaaaa;
  --light:#f5f5f5;
  --cream:#fffbf0;
  --ink:#111111;
  --text:#333333;
  --btn:#6b6b6b;
  --navy:#2d3448;
}
*{box-sizing:border-box;margin:0;padding:0}
html,body{width:1200px;height:2773px;overflow:hidden}
body{position:relative;background:var(--white);font-family:'Roboto',sans-serif;color:var(--text)}
.abs{position:absolute}
.head{font-family:'Bebas Neue',sans-serif;letter-spacing:1.5px;color:var(--ink);text-align:center}
.btn{position:absolute;left:525px;width:150px;height:38px;background:var(--btn);color:var(--white);font-family:'Roboto',sans-serif;font-weight:500;font-size:11px;letter-spacing:1px;display:flex;align-items:center;justify-content:center;gap:8px}
.brand-box{position:absolute;width:100px;height:100px;border:2px solid var(--white);display:flex;align-items:center;justify-content:center;text-align:center;color:var(--white);font-family:'Roboto',sans-serif;font-size:14px;line-height:1.05}
.hero{position:absolute;left:0;top:0;width:1200px;height:560px;overflow:hidden}
.hero-photo{position:absolute;inset:0;background:linear-gradient(135deg,#4a4a52 0%,#6e6258 35%,#857040 50%,#4f4c50 70%,#2e2e34 100%)}
.hero-shade{position:absolute;inset:0;background:rgba(0,0,0,.28)}
.nav{position:absolute;top:49px;left:0;width:1200px;height:16px;font-size:12px;font-weight:500;color:var(--white);letter-spacing:.5px}
.nav span{position:absolute;top:0}
.hero-title{position:absolute;top:232px;width:1200px;font-size:58px;color:var(--white)}
.hero-sub{position:absolute;top:300px;width:1200px;font-size:23px;color:var(--white)}
.slide-arrow{position:absolute;top:287px;width:32px;height:28px;background:rgba(255,255,255,.35);display:flex;align-items:center;justify-content:center}
.frame{position:absolute;width:100px;height:100px;border:2px solid var(--navy)}
.sec-title{position:absolute;width:1200px;font-size:37px;line-height:35px}
.copy{position:absolute;left:290px;width:620px;font-size:12.5px;line-height:19px;text-align:center;color:var(--text)}
.video{position:absolute;left:0;top:1087px;width:1200px;height:457px;background:radial-gradient(ellipse at 50% 80%,#9b8a5a 0%,#5a5a5a 30%,#3c3c3c 70%,#2a2a2a 100%)}
.card{position:absolute;top:1586px;width:204px;height:276px;background:linear-gradient(160deg,#5c5c5c,#3e3e3e 60%,#555)}
.card-label{position:absolute;top:112px;width:204px;text-align:center;color:var(--white);font-size:25px;line-height:27px}
.card-label b{font-weight:500;display:block}
.partner{position:absolute;top:2072px;width:150px;height:36px;display:flex;align-items:center;justify-content:center;color:#444;font-family:'Roboto',sans-serif;font-weight:500;font-size:18px;letter-spacing:.5px}
.rule{position:absolute;left:161px;top:2156px;width:878px;height:1px;background:#cfcfcf}
.field{position:absolute;left:438px;top:2345px;width:272px;height:44px;background:var(--light);font-size:11px;color:#666;padding-left:18px;display:flex;align-items:center}
.send{position:absolute;left:710px;top:2345px;width:50px;height:44px;background:var(--mid);display:flex;align-items:center;justify-content:center}
.footer{position:absolute;left:0;top:2437px;width:1200px;height:336px;background:var(--mid)}
.foot-text{position:absolute;width:1200px;text-align:center;color:var(--white);font-size:13px;line-height:21px}
.social{position:absolute;top:2655px;width:26px;height:26px;border-radius:50%;background:var(--white)}
.small{font-size:10px;line-height:17px}
</style>
</head>
<body>

<header class="hero">
  <div class="hero-photo" role="img" aria-label="Photo of young people using phones and a tablet"></div>
  <div class="hero-shade"></div>
  <div class="brand-box" style="left:161px;top:22px">Harlow<br>Crest<br>Studio</div>
  <nav class="nav">
    <span style="left:692px">WORK</span>
    <span style="left:749px">SERVIC</span>
    <span style="left:826px">ABOU</span>
    <span style="left:889px">BLOG</span>
    <span style="left:950px">CONTACT</span>
    <svg style="position:absolute;left:1022px;top:0" width="16" height="16" viewBox="0 0 16 16"><circle cx="6.5" cy="6.5" r="5" fill="none" stroke="#fff" stroke-width="2"/><line x1="10" y1="10" x2="15" y2="15" stroke="#fff" stroke-width="2"/></svg>
  </nav>
  <h1 class="head hero-title">LET’S START WORK TOGATHER</h1>
  <p class="head hero-sub">A STARTUP COMPANY PROVIDE YOU ALL KIND OF ONLINE SERVICES</p>
  <div class="btn" style="top:349px">EXPLORE US <span>→</span></div>
  <div class="slide-arrow" style="left:0"><svg width="10" height="14"><path d="M8 1 L2 7 L8 13" fill="none" stroke="#fff" stroke-width="2"/></svg></div>
  <div class="slide-arrow" style="left:1168px"><svg width="10" height="14"><path d="M2 1 L8 7 L2 13" fill="none" stroke="#fff" stroke-width="2"/></svg></div>
</header>

<section class="services">
  <svg class="abs" style="left:0;top:800px" width="1200" height="287" viewBox="0 0 1200 287">
    <path d="M0 40 C150 -10 260 60 420 50 C560 40 640 -5 800 20 C960 45 1060 90 1200 30 L1200 287 L0 287 Z" fill="#f3f3f3"/>
    <path d="M0 120 C120 80 220 30 380 60 C520 90 600 40 740 60 C900 85 1000 140 1200 100 L1200 287 L0 287 Z" fill="#ececec"/>
  </svg>
  <div class="frame" style="left:549px;top:610px"></div>
  <h2 class="head sec-title" style="top:630px">BEST DIGITAL<br>MARKETING SERVICES!</h2>
  <p class="copy" style="top:738px">Lorem ipsum dolor sit amet, consectetur adipiscing elit. Duis posuere tincidunt odio quis euismod. Maecenas ac erat eu leo sagittis pellentesque. Fusce pulvinar tristique quam, eget dictum felis rhoncus in. Aliquam erat volutpat. In sit amet velit laoreet, ultrices risus ac.</p>
  <svg class="abs" style="left:578px;top:828px" width="44" height="44" viewBox="0 0 44 44"><rect x="4" y="14" width="12" height="16" fill="#3a4aa8"/><path d="M16 14 L34 4 L34 40 L16 30 Z" fill="#5566c8"/><circle cx="38" cy="22" r="3" fill="#e04a4a"/></svg>
  <h3 class="head abs" style="top:884px;width:1200px;font-size:24px">SOCAIL MARKETING</h3>
  <p class="copy" style="top:925px">Phasellus sollicitudin ligula eu ex pharetra aliquam. Quisque nec nisl ut neque auctor sagittis. Vestibulum pellentesque dui turpis, et gravida nisl mattis quis. Quisque eu mi nec nunc tincidunt varius. Praesent varius feugiat justo. Proin sed sodales est. Donec blandit ultricies erat. Nunc sagittis lectus et augue tristique condimentum.</p>
  <div class="btn" style="top:1022px">READ MORE</div>
</section>

<section>
  <div class="video" role="img" aria-label="Video still of hands on a tablet with digital marketing icons"></div>
  <svg class="abs" style="left:560px;top:1281px" width="74" height="74" viewBox="0 0 74 74"><circle cx="37" cy="37" r="33" fill="none" stroke="#fff" stroke-width="5"/><path d="M29 22 L52 37 L29 52 Z" fill="#fff"/></svg>
</section>

<section class="work">
  <div class="card" style="left:161px" role="img" aria-label="Portfolio photo of a woman at a laptop"><div class="card-label">Company<b>LOGO</b></div></div>
  <div class="card" style="left:386px" role="img" aria-label="Portfolio photo of a woman at a laptop"><div class="card-label">Company<b>LOGO</b></div></div>
  <div class="card" style="left:612px" role="img" aria-label="Portfolio photo of a woman at a laptop"><div class="card-label">Company<b>LOGO</b></div></div>
  <div class="card" style="left:836px" role="img" aria-label="Portfolio photo of a woman at a laptop"><div class="card-label">Company<b>LOGO</b></div></div>
  <div class="btn" style="top:1899px">VIEW MORE</div>
</section>

<section class="brands">
  <h2 class="head abs" style="top:1976px;width:1200px;font-size:36px">BRAND EXPERIENCES IN PROGRESS</h2>
  <div class="partner" style="left:171px">CLIENT ONE</div>
  <div class="partner" style="left:350px">CLIENT TWO</div>
  <div class="partner" style="left:524px">CLIENT THREE</div>
  <div class="partner" style="left:704px">CLIENT FOUR</div>
  <div class="partner" style="left:877px">CLIENT FIVE</div>
  <div class="rule"></div>
</section>

<section class="newsletter">
  <div class="frame" style="left:549px;top:2204px"></div>
  <h2 class="head sec-title" style="top:2224px">NEED TO KNOW OUR NEWS DAILY?<br>SUBSCRIBE TO OUR NEWSLETTER TODAY.</h2>
  <div class="field">Enter your email address</div>
  <div class="send"><svg width="18" height="18" viewBox="0 0 18 18"><path d="M1 8 L17 1 L10 17 L8 10 Z" fill="none" stroke="#fff" stroke-width="1.5"/></svg></div>
</section>

<footer>
  <div class="footer"></div>
  <div class="brand-box" style="left:551px;top:2483px">Harlow<br>Crest<br>Studio</div>
  <p class="foot-text" style="top:2605px">Duis autem vel eum iriure dolor in hendrerit in vulputate velit esse molestie<br>consequat, vel illum dolore</p>
  <span class="social" style="left:523px"></span>
  <span class="social" style="left:555px"></span>
  <span class="social" style="left:587px"></span>
  <span class="social" style="left:619px"></span>
  <span class="social" style="left:651px"></span>
  <p class="foot-text small" style="top:2698px">© Copyright 2018, Harlow Crest Studio<br>All Rights Reserved</p>
</footer>

</body>
</html>
```